The Ashdale Clinic Business Card

We need a new business card design for a rehabilitation center in California. Please use the branding from the logo.

Use the attached logo.

Target Market(s)

Physicians referring patients

Industry/Entity Type

Business

Contact Information for Business Card

Updated business cards for new brand

Font styles to use
Sans Serif

Colors
0255a3
3176b5
85abd2
fece3e

Requirements
Must have
• The logo: front and back
• website url: www.TheAshdaleClinic.example
• Full Name: Daniel Harwood
• Title: Chief Financial Officer
• Email: dharwood@theashdaleclinic.example
• Office: 555.014.2738
• Cell: 555.016.4821
• Fax: 555.019.3057
Nice to have
• Icons
Should not have
• whimsical fonts

```html
<!DOCTYPE html>
<html lang="en">
<head>
<meta charset="utf-8">
<title>The Ashdale Clinic Business Card</title>
<link href="https://fonts.googleapis.com/css2?family=Arimo:wght@400;700&display=swap" rel="stylesheet">
<style>
  :root {
    --brand-blue: #2f78b4;
    --ink: #1e1a1a;
    --card-line: #6b6b6b;
    --paper: #ffffff;
    --divider: #7a7a7a;
  }
  html, body {
    margin: 0;
    padding: 0;
    width: 1200px;
    height: 1200px;
    overflow: hidden;
    background: var(--paper);
    font-family: "Arimo", Arial, sans-serif;
  }
  .canvas {
    position: relative;
    width: 1200px;
    height: 1200px;
  }
  .card {
    position: absolute;
    left: 180px;
    width: 838px;
    height: 478px;
    border-radius: 38px;
    box-sizing: border-box;
  }
  .card-front {
    top: 100px;
    background: var(--brand-blue);
    color: var(--paper);
  }
  .front-brand {
    position: absolute;
    left: 0;
    right: 0;
    top: 178px;
    display: flex;
    align-items: center;
    justify-content: center;
    gap: 20px;
    font-size: 52px;
    font-weight: 400;
    color: var(--paper);
  }
  .front-brand .mark-square {
    width: 40px;
    height: 40px;
    background: var(--paper);
  }
  .front-url {
    position: absolute;
    left: 0;
    right: 0;
    top: 408px;
    text-align: center;
    font-size: 25px;
    letter-spacing: 0.1px;
  }
  .card-back {
    top: 618px;
    background: var(--paper);
    border: 1px solid var(--card-line);
  }
  .back-brand {
    position: absolute;
    left: 52px;
    top: 222px;
    display: flex;
    align-items: center;
    gap: 12px;
    font-size: 27px;
    font-weight: 700;
    color: var(--brand-blue);
    white-space: nowrap;
  }
  .back-brand .mark-square {
    width: 22px;
    height: 22px;
    background: var(--brand-blue);
  }
  .divider {
    position: absolute;
    left: 353px;
    top: 94px;
    width: 1.5px;
    height: 292px;
    background: var(--divider);
  }
  .person {
    position: absolute;
    left: 379px;
    top: 106px;
    color: var(--ink);
  }
  .person-name {
    margin: 0;
    font-size: 32px;
    font-weight: 700;
    line-height: 1.1;
  }
  .person-title {
    margin: 4px 0 0;
    font-size: 21px;
    font-weight: 400;
  }
  .contacts {
    position: absolute;
    left: 379px;
    top: 199px;
    margin: 0;
    padding: 0;
    list-style: none;
    color: var(--ink);
    font-size: 23px;
  }
  .contacts li {
    display: flex;
    align-items: center;
    height: 36px;
    white-space: nowrap;
  }
  .contacts svg {
    width: 24px;
    height: 24px;
    margin-right: 18px;
    flex: none;
    fill: var(--brand-blue);
  }
</style>
</head>
<body>
<main class="canvas">
  <section class="card card-front">
    <div class="front-brand"><span class="mark-square"></span>The Ashdale Clinic</div>
    <div class="front-url">www.TheAshdaleClinic.example</div>
  </section>

  <section class="card card-back">
    <div class="back-brand"><span class="mark-square"></span>The Ashdale Clinic</div>
    <div class="divider"></div>
    <div class="person">
      <h1 class="person-name">Daniel Harwood</h1>
      <p class="person-title">Chief Financial Officer</p>
    </div>
    <ul class="contacts">
      <li>
        <svg viewBox="0 0 24 24" aria-label="Office"><path d="M2 10c3-4 17-4 20 0l-1 3h-4l-1-2c-2-.6-6-.6-8 0l-1 2H3z"/><circle cx="12" cy="15.5" r="4"/><circle cx="12" cy="15.5" r="1.8" fill="#fff"/></svg>
        555.014.2738
      </li>
      <li>
        <svg viewBox="0 0 24 24" aria-label="Cell"><path d="M7 1h10a2 2 0 0 1 2 2v18a2 2 0 0 1-2 2H7a2 2 0 0 1-2-2V3a2 2 0 0 1 2-2zm0 3v14h10V4z"/><circle cx="12" cy="20.5" r="1.2" fill="#fff"/></svg>
        555.016.4821
      </li>
      <li>
        <svg viewBox="0 0 24 24" aria-label="Fax"><path d="M7 1h8l3 3v8H7z"/><path d="M2 13h20v6H2zM1 20h22v3H1z"/><rect x="9" y="5" width="6" height="1.4" fill="#fff"/><rect x="9" y="8" width="6" height="1.4" fill="#fff"/></svg>
        555.019.3057
      </li>
      <li>
        <svg viewBox="0 0 24 24" aria-label="Email"><path d="M1 5h22v14H1z"/><path d="M2 6l10 8 10-8M2 18l7-6M22 18l-7-6" stroke="#fff" stroke-width="1.5" fill="none"/></svg>
        dharwood@theashdaleclinic.example
      </li>
      <li>
        <svg viewBox="0 0 24 24" aria-label="Website"><circle cx="12" cy="12" r="11"/><g stroke="#fff" stroke-width="1.4" fill="none"><ellipse cx="12" cy="12" rx="4.5" ry="10"/><path d="M12 2v20M2 12h20M4 7h16M4 17h16"/></g></svg>
        www.TheAshdaleClinic.example
      </li>
    </ul>
  </section>
</main>
</body>
</html>
```